Halvex Consulting

Hi,
I have my own network consulting business (just me)
and need to get a logo and business card design together,

Based in New Zealand,

Gareth Pollard
Unified Communications and Network Architect

/design engineer,
and would like this to be the basis for personal branding and company identity

Reason: I will be off site for a couple of days - so you have some more time

Business

• I have the basis for a optional logo - needs color -

```html
<!DOCTYPE html>
<html lang="en">
<head>
<meta charset="utf-8">
<title>Gareth Pollard — Halvex Consulting</title>
<link rel="stylesheet" href="https://fonts.googleapis.com/css2?family=Comfortaa:wght@400;700&display=swap">
<style>
  :root {
    --page: #ffffff;
    --card-top: #2a2a2a;
    --card-bottom: #333333;
    --band-top: #4a4a4a;
    --band-bottom: #444444;
    --lime-light: #c4e45a;
    --lime-dark: #86ba1c;
    --lime: #8cc63f;
    --subtitle: #e2e2e2;
  }
  * { margin: 0; padding: 0; box-sizing: border-box; }
  html, body {
    width: 1200px;
    height: 900px;
    overflow: hidden;
    background: var(--page);
  }
  .card {
    position: absolute;
    left: 70px;
    top: 156px;
    width: 1060px;
    height: 588px;
    background: linear-gradient(180deg, var(--card-top), var(--card-bottom));
    overflow: hidden;
    font-family: "Comfortaa", sans-serif;
  }
  .card__texture {
    position: absolute;
    inset: 0;
    width: 100%;
    height: 100%;
  }
  .card__band {
    position: absolute;
    left: 0;
    top: 0;
    width: 100%;
    height: 100%;
  }
  .identity {
    position: absolute;
    left: 0;
    right: 0;
    top: 192px;
    text-align: center;
  }
  .identity__name {
    font-size: 98px;
    font-weight: 700;
    letter-spacing: 3px;
    line-height: 1;
    background: linear-gradient(180deg, var(--lime-light), var(--lime-dark));
    -webkit-background-clip: text;
    background-clip: text;
    color: transparent;
  }
  .identity__role {
    margin-top: 18px;
    font-size: 24px;
    font-weight: 400;
    font-variant: small-caps;
    letter-spacing: 3.5px;
    color: var(--subtitle);
  }
  .brand {
    position: absolute;
    left: 22px;
    top: 492px;
    display: flex;
    align-items: center;
    gap: 20px;
  }
  .brand__dot {
    width: 46px;
    height: 46px;
    border-radius: 50%;
    background: var(--lime);
  }
  .brand__name {
    font-size: 60px;
    font-weight: 700;
    color: var(--lime);
    line-height: 1;
  }
</style>
</head>
<body>
  <div class="card">
    <div class="card__texture" role="img" aria-label="Fine diagonal line texture across the card background"></div>
    <svg class="card__band" viewBox="0 0 1060 588" preserveAspectRatio="none" aria-hidden="true">
      <defs>
        <linearGradient id="band-fill" x1="0" y1="0" x2="0" y2="1">
          <stop offset="0" stop-color="var(--band-top)"/>
          <stop offset="1" stop-color="var(--band-bottom)"/>
        </linearGradient>
      </defs>
      <path d="M0 440 Q530 400 1060 440 L1060 588 L0 588 Z" fill="url(#band-fill)"/>
    </svg>

    <div class="identity">
      <h1 class="identity__name">Gareth Pollard</h1>
      <p class="identity__role">Unified Communications and Network Architect</p>
    </div>

    <div class="brand">
      <span class="brand__dot"></span>
      <span class="brand__name">halvex</span>
    </div>
  </div>
</body>
</html>
```